I need a two page flyer (one page front and back) outlining our residential furniture rental options.

Title: Premium Residential Furniture Rentals

GOOD
Our Brimwell Orla Furniture Package is designed to offer a perfect balance of affordability and style, without compromising on quality. This package features a selection of functional and aesthetically pleasing furniture pieces, ideal for those looking to create a polished and professional space. With quick installation handled by our experienced in-house team, you can expect a smooth and hassle-free setup. This package ensures both convenience and value, providing a streamlined solution for your needs.
Living room, dining room and bedroom (additional bedrooms available)
- $710/month with a 3 month commitment
- $570/month with a 6 month commitment

BETTER
Our Premium Furniture Package takes comfort and style to the next level, offering an enhanced experience compared to our Orla option. Carefully selected with durability in mind, this package features high-quality, convenient furniture designed for both functionality and aesthetics. Perfect for those seeking a more refined look and superior comfort, it’s ideal for creating a sophisticated and inviting environment. With attention to detail in both design and craftsmanship, the premium package elevates any space, ensuring a higher standard of comfort and style that caters to both employees and clients.
- $1,150/month with a 3 month commitment
- $900/month with a 6 month commitment

BEST
Our Custom Furniture Package offers a tailored experience where you’ll work directly with our expert designer to create the ultimate luxurious and functional space. We include lounging, dining, sleeping and working from home, this package allows you to curate a space that perfectly fits your needs and style. With personalized attention to detail, we ensure every element is designed to provide the highest level of comfort, convenience, and elegance, transforming your space into a sophisticated sanctuary for relaxation and enjoyment.
Please inquire for pricing

www.quilbyhomeleasing.com

```html
<!DOCTYPE html>
<html lang="en">
<head>
<meta charset="utf-8">
<title>Quilby Home Leasing – Residential Furniture Rentals Flyer</title>
<link rel="stylesheet" href="https://fonts.googleapis.com/css2?family=Oswald:wght@500;600&family=Montserrat:wght@400;600;700&family=Open+Sans:wght@400;600;700&display=swap">
<style>
  :root {
    --backdrop: #d9d2cd;
    --paper: #ffffff;
    --cream: #f3e6d6;
    --tan: #e3c69d;
    --brown: #7d5f3c;
    --ink: #3b3530;
    --charcoal: #3a3a3a;
    --navy: #1f2a5c;
    --outline: #ffffff;
  }
  * { box-sizing: border-box; margin: 0; padding: 0; }
  html, body { width: 1200px; height: 447px; overflow: hidden; background: var(--backdrop); }
  .spread {
    width: 1200px; height: 447px;
    display: flex; justify-content: center; align-items: center; gap: 40px;
  }
  .sheet-slot { width: 297px; height: 421px; position: relative; box-shadow: 0 3px 10px rgba(0,0,0,.18); }
  .sheet {
    position: absolute; top: 0; left: 0;
    width: 587px; height: 832px;
    transform: scale(0.506); transform-origin: 0 0;
    overflow: hidden;
  }

  /* ---------- FRONT ---------- */
  .front { background: var(--paper); }
  .brand { position: absolute; left: 0; width: 265px; top: 40px; text-align: center; }
  .brand-mark { display: block; width: 30px; height: 30px; margin: 0 auto 14px; background: var(--navy); }
  .brand-name {
    font-family: "Montserrat", sans-serif; font-weight: 600; font-size: 18px;
    color: var(--navy); letter-spacing: 1px; text-transform: uppercase;
  }
  .brand-services {
    margin-top: 16px; font-family: "Montserrat", sans-serif; font-weight: 600;
    font-size: 8px; color: var(--navy); letter-spacing: .6px;
  }
  .front-panel { position: absolute; left: 284px; top: 82px; width: 303px; height: 669px; background: var(--tan); }
  .front-title {
    position: absolute; left: 298px; top: 104px; width: 285px;
    font-family: "Oswald", sans-serif; font-weight: 600; font-size: 34px; line-height: 34px;
    color: var(--brown); letter-spacing: .3px;
  }
  .tier-label {
    font-family: "Oswald", sans-serif; font-weight: 600; color: var(--charcoal);
    letter-spacing: 1px; line-height: 1;
  }
  .front .tier-label { position: absolute; left: 17px; top: 172px; font-size: 34px; }
  .front-photo {
    position: absolute; left: 0; top: 208px; width: 392px; height: 448px;
    background: linear-gradient(120deg, #e9e6e0 0%, #cfc4b2 40%, #a89a86 70%, #5d554d 100%);
  }
  .front-photo-tint { position: absolute; left: 284px; top: 208px; width: 108px; height: 448px; background: var(--tan); opacity: .45; }
  .front-copy {
    position: absolute; left: 407px; top: 203px; width: 162px;
    font-family: "Open Sans", sans-serif; font-size: 12.6px; line-height: 18.7px;
    color: var(--ink); text-align: justify;
  }
  .rooms-note {
    position: absolute; left: 307px; top: 686px; width: 270px;
    font-family: "Oswald", sans-serif; font-weight: 500; font-size: 15.5px; line-height: 18px; color: var(--brown);
  }
  .price-box {
    position: absolute; border: 2.5px solid var(--charcoal); background: var(--paper);
    text-align: center; color: var(--charcoal);
    font-family: "Open Sans", sans-serif; font-size: 10.5px; line-height: 10px; padding-top: 6px;
  }
  .price-box .amount { display: block; font-family: "Oswald", sans-serif; font-weight: 600; font-size: 16px; line-height: 18px; }
  .front .price-box { top: 680px; width: 73px; height: 73px; }
  .site-url { font-family: "Montserrat", sans-serif; font-weight: 700; letter-spacing: .2px; }
  .front .site-url { position: absolute; left: 0; width: 587px; top: 794px; text-align: center; font-size: 20px; color: var(--charcoal); }

  /* ---------- BACK ---------- */
  .back { background: var(--cream); }
  .frame { position: absolute; border: 2px solid var(--outline); }
  .good-label {
    position: absolute; left: 80px; top: 52px;
    font-family: "Montserrat", sans-serif; font-weight: 700; font-size: 31px; color: var(--navy);
  }
  .good-copy {
    position: absolute; left: 207px; top: 17px; width: 363px;
    font-family: "Open Sans", sans-serif; font-size: 10.4px; line-height: 14.3px; color: var(--ink); text-align: justify;
  }
  .good-rooms {
    position: absolute; left: 230px; width: 316px; top: 134px; text-align: center;
    font-family: "Open Sans", sans-serif; font-weight: 700; font-size: 10.5px; line-height: 16px; color: var(--navy);
  }
  .bedroom-photo {
    position: absolute; left: 22px; top: 163px; width: 390px; height: 225px;
    background: radial-gradient(ellipse at 45% 60%, #56616a 0%, #3c4650 35%, #a9adaf 65%, rgba(243,230,214,0) 82%);
  }
  .back .site-url { position: absolute; left: 147px; top: 394px; font-size: 14.5px; color: var(--navy); }
  .back .price-box { border-color: var(--navy); color: var(--navy); top: 336px; width: 73px; height: 73px; background: var(--cream); }
  .back .price-box .amount { color: var(--navy); }
  .best-tab { position: absolute; left: 0; top: 425px; width: 114px; height: 46px; background: var(--tan); }
  .back .tier-label { position: absolute; left: 18px; top: 431px; font-size: 32px; }
  .best-copy {
    position: absolute; left: 18px; top: 471px; width: 184px;
    font-family: "Open Sans", sans-serif; font-size: 10.4px; line-height: 14.2px; color: var(--ink); text-align: justify;
  }
  .living-photo {
    position: absolute; left: 211px; top: 456px; width: 360px; height: 362px;
    background: linear-gradient(170deg, #efe8dc 0%, #c9b8a0 35%, #9b9790 65%, #6b6a68 100%);
  }
  .shelf-photo {
    position: absolute; left: 64px; top: 720px; width: 108px; height: 106px;
    background: linear-gradient(160deg, #e6d98e 0%, #b79d68 45%, #6d5a44 100%);
  }
  .inquire-box {
    position: absolute; left: 228px; top: 705px; width: 72px; height: 75px;
    background: rgba(40,40,40,.85); border: 2px solid #ffffff;
    color: #ffffff; text-align: center;
    font-family: "Open Sans", sans-serif; font-weight: 700; font-size: 11.5px; line-height: 15px;
    display: flex; align-items: center; justify-content: center;
  }
</style>
</head>
<body>
<main class="spread">

  <!-- Front page -->
  <div class="sheet-slot">
    <section class="sheet front" aria-label="Flyer front">
      <div class="brand">
        <span class="brand-mark"></span>
        <div class="brand-name">Quilby Home Leasing</div>
        <div class="brand-services">STAGING | RESIDENTIAL | CORPORATE | SALES</div>
      </div>
      <div class="front-panel"></div>
      <h1 class="front-title">Premium Residential Furniture Rentals</h1>
      <h2 class="tier-label">BETTER</h2>
      <div class="front-photo" role="img" aria-label="Photo of a staged living room with cream sofa, round coffee tables and large abstract wall art"></div>
      <div class="front-photo-tint"></div>
      <p class="front-copy">Our Premium Furniture Package takes comfort and style to the next level, offering an enhanced experience compared to our Orla option. Carefully selected with durability in mind, this package features high-quality, convenient furniture designed for both functionality and aesthetics. Perfect for those seeking a more refined look and superior comfort, it’s ideal for creating a sophisticated and inviting environment. With attention to detail in both design and craftsmanship, the premium package elevates any space, ensuring a higher standard of comfort and style that caters to both employees and clients.</p>
      <div class="price-box" style="left:82px"><span class="amount">$1,150</span>month<br>with a<br>3 month<br>commitment</div>
      <div class="price-box" style="left:162px"><span class="amount">$900</span>month<br>with a<br>6 month<br>commitment</div>
      <p class="rooms-note">Living room, Dining room and Bedroom<br>(additional bedrooms available)</p>
      <p class="site-url">www.quilbyhomeleasing.com</p>
    </section>
  </div>

  <!-- Back page -->
  <div class="sheet-slot">
    <section class="sheet back" aria-label="Flyer back">
      <div class="frame" style="left:48px;top:20px;width:66px;height:102px"></div>
      <h2 class="good-label">GOOD</h2>
      <p class="good-copy">Our Brimwell Orla Furniture Package is designed to offer a perfect balance of affordability and style, without compromising on quality. This package features a selection of functional and aesthetically pleasing furniture pieces, ideal for those looking to create a polished and professional space. With quick installation handled by our experienced in-house team, you can expect a smooth and hassle-free setup. This package ensures both convenience and value, providing a streamlined solution for your needs.</p>
      <p class="good-rooms">Living room, dining room and bedroom<br>(additional bedrooms available)</p>
      <div class="frame" style="left:430px;top:175px;width:80px;height:70px"></div>
      <div class="frame" style="left:5px;top:330px;width:65px;height:70px"></div>
      <div class="bedroom-photo" role="img" aria-label="Product photo of a bedroom set: tufted dark headboard bed, nightstand with lamp and grey dresser"></div>
      <p class="site-url">www.quilbyhomeleasing.com</p>
      <div class="price-box" style="left:413px"><span class="amount">$710</span>month<br>with a<br>3 month<br>commitment</div>
      <div class="price-box" style="left:493px"><span class="amount">$570</span>month<br>with a<br>6 month<br>commitment</div>

      <div class="best-tab"></div>
      <h2 class="tier-label">BEST</h2>
      <p class="best-copy">Our Custom Furniture Package offers a tailored experience where you’ll work directly with our expert designer to create the ultimate luxurious and functional space. We include lounging, dining, sleeping and working from home, this package allows you to curate a space that perfectly fits your needs and style. With personalized attention to detail, we ensure every element is designed to provide the highest level of comfort, convenience, and elegance, transforming your space into a sophisticated sanctuary for relaxation and enjoyment.</p>
      <div class="frame" style="left:530px;top:425px;width:46px;height:60px"></div>
      <div class="living-photo" role="img" aria-label="Photo of a furnished living room with grey sectional sofa, fireplace, lit shelves and pendant lantern"></div>
      <div class="inquire-box">Please<br>inquire<br>for pricing</div>
      <div class="frame" style="left:44px;top:705px;width:60px;height:60px"></div>
      <div class="shelf-photo" role="img" aria-label="Photo of a lit display shelf with decor above a wooden console"></div>
    </section>
  </div>

</main>
</body>
</html>
```